New Business Card Design Project

We are looking for a talented individual to create a truly awesome/unique business card design for us. We are looking for a someone to design something that will really stand out from the crowd - we don't mind what ideas you come up with (ie embossed/flat/matte/shine etc etc) just wow us with your creativity.
Updates

Target Market(s)

Video Games Industry Professionals (all levels of seniority from QA Testers through to CEOs)

Contact Information for Business Card

Company logo (see upload)
Company name: Northbay Play Careers Ltd
Employee Name: Darren Elsby
Job title: CEO
Website: www.nbpc2go.example
Office +44 1632 960418
Mobile: +44 7700 900276
Email: darren@nbpc2go.example

Colors

Designer to choose colors to be used in the design.

Requirements
Must have
• The business card design MUST contain all the information listed in the BUSINESS CARD DETAILS box.
• You will see the colours that are relevant to us (ie company logo) in the uploaded imagery - however you do not have to use all these colours when designing the business card itself
• MUST BE DOUBLE SIDED

```html
<!DOCTYPE html>
<html lang="en">
<head>
<meta charset="utf-8">
<title>Northbay Play Careers – Business Card</title>
<link rel="stylesheet" href="https://fonts.googleapis.com/css2?family=Montserrat:wght@700;800&family=Lato:wght@400;700&display=swap">
<style>
  :root {
    --navy: #1d2d5c;
    --orange: #f47c20;
    --paper: #ffffff;
    --ink: #222633;
    --backdrop: #e9e6e1;
    --heading: "Montserrat", Arial, sans-serif;
    --body: "Lato", Arial, sans-serif;
  }
  * { box-sizing: border-box; margin: 0; padding: 0; }
  html, body { width: 1200px; height: 910px; overflow: hidden; }
  body {
    background: var(--backdrop);
    display: flex;
    flex-direction: column;
    align-items: center;
    justify-content: center;
    gap: 40px;
  }
  .card {
    position: relative;
    width: 700px;
    height: 400px;
    overflow: hidden;
    box-shadow: 0 4px 14px rgba(0,0,0,.18);
  }

  /* Back side */
  .card--back { background: var(--navy); }
  .card--back .mascot {
    position: absolute;
    left: 150px; top: 95px;
    width: 170px; height: 150px;
    border-radius: 12px;
    background: radial-gradient(circle at 55% 50%, rgba(255,255,255,.55), rgba(255,255,255,.12) 70%);
  }
  .card--back .brand {
    position: absolute;
    left: 340px; top: 160px;
    font-family: var(--heading);
    font-weight: 800;
    font-size: 34px;
    line-height: 1.05;
    color: var(--paper);
  }
  .card--back .site {
    position: absolute;
    left: 0; right: 0; bottom: 70px;
    text-align: center;
    font-family: var(--body);
    font-size: 17px;
    letter-spacing: .04em;
    color: var(--paper);
  }
  .site .domain { color: var(--orange); }

  /* Front side */
  .card--front { background: var(--paper); }
  .card--front .mascot {
    position: absolute;
    left: 0; top: 40px;
    width: 300px; height: 330px;
    border-radius: 0 40% 40% 0;
    background: linear-gradient(135deg, var(--navy), #3a4b80 60%, #c9cedd);
  }
  .card--front .details {
    position: absolute;
    left: 350px; top: 60px;
    right: 30px;
  }
  .card--front .brand {
    font-family: var(--heading);
    font-weight: 800;
    font-size: 30px;
    line-height: 1.05;
    color: var(--navy);
    margin-bottom: 26px;
  }
  .person-name {
    font-family: var(--heading);
    font-weight: 700;
    font-size: 22px;
    letter-spacing: .04em;
    text-transform: uppercase;
    color: var(--navy);
  }
  .person-role {
    font-family: var(--body);
    font-size: 16px;
    color: var(--ink);
    margin-bottom: 22px;
  }
  .contacts { list-style: none; font-family: var(--body); font-size: 17px; color: var(--ink); }
  .contacts li { display: flex; align-items: center; gap: 10px; line-height: 1.55; }
  .contacts svg { width: 16px; height: 16px; flex: none; }
  .card--front .site {
    margin-top: 20px;
    font-family: var(--body);
    font-weight: 700;
    font-size: 20px;
    color: var(--ink);
    display: flex; align-items: center; gap: 8px;
  }
  .site svg { width: 26px; height: 26px; }
</style>
</head>
<body>

<section class="card card--back" aria-label="Business card back">
  <div class="mascot" role="img" aria-label="Mascot illustration in white on navy"></div>
  <div class="brand">Northbay Play<br>Careers</div>
  <p class="site">www.<span class="domain">nbpc2go</span>.example</p>
</section>

<section class="card card--front" aria-label="Business card front">
  <div class="mascot" role="img" aria-label="Large navy mascot illustration"></div>
  <div class="details">
    <div class="brand">Northbay Play<br>Careers</div>
    <p class="person-name">Darren Elsby</p>
    <p class="person-role">CEO</p>
    <ul class="contacts">
      <li>
        <svg viewBox="0 0 16 16" aria-hidden="true"><rect x="4" y="1" width="8" height="14" rx="1.5" fill="none" stroke="var(--orange)" stroke-width="1.6"/><circle cx="8" cy="12.3" r=".9" fill="var(--orange)"/></svg>
        +44 7700 900276
      </li>
      <li>
        <svg viewBox="0 0 16 16" aria-hidden="true"><path d="M4 1.5l2.2 3-1.4 1.6c.8 1.9 2.2 3.4 4.1 4.3l1.6-1.4 3 2.2-1.3 2.6C7 13.4 2.6 9 1.4 2.8z" fill="var(--orange)"/></svg>
        +44 1632 960418
      </li>
      <li>
        <svg viewBox="0 0 16 16" aria-hidden="true"><rect x="1" y="3.5" width="14" height="9.5" rx="1" fill="var(--orange)"/><path d="M1.5 4l6.5 5 6.5-5" fill="none" stroke="#fff" stroke-width="1.3"/></svg>
        darren@nbpc2go.example
      </li>
    </ul>
    <p class="site">
      <span>www.<span class="domain">nbpc2go</span>.example</span>
      <svg viewBox="0 0 26 26" aria-hidden="true">
        <g stroke="var(--orange)" stroke-width="1.6" stroke-linecap="round"><path d="M8 2v3M2 8h3M3.5 3.5l2 2M12.5 3.5l-2 2M3.5 12.5l2-2"/></g>
        <path d="M9 9l3 14 3-5.5 5 5 2.2-2.2-5-5L22.5 12z" fill="#fff" stroke="var(--ink)" stroke-width="1.5" stroke-linejoin="round"/>
      </svg>
    </p>
  </div>
</section>

</body>
</html>
```